Business cards and stationary for training company
Company in Japan specializing in corporate training
Business cards and stationary for training company  - Corporate Services
Creative Brief
Use specific fonts
Please help with this
Professional
Brandon Mallory
President
4-17-3 Hoshimidai, Adachi, Tokyo 123-0845
brandon@brightpathlearninggroup.example
BrightPathLearningGroup.example
Will update information soon
I'm thinking to use one side for logo and other for contact info, however I need English and Japanese writing
Concepts
Business Cards and Stationery for new compliance company.
Business Cards and Stationery for Background Check Company
Leftnut Leftnut
Thank you everyone for the great designs. I will be using the stationary for rinted material and would need to think printer friendly. Thus, would it be possible to see letter head with a simple design that will look good in a thirty page booklet? Thank you.
Great so far, however it would great to see some stationary

```html
<!DOCTYPE html>
<html lang="en">
<head>
<meta charset="utf-8">
<title>BrightPath Learning Group — Business Card</title>
<link rel="stylesheet" href="https://fonts.googleapis.com/css2?family=Open+Sans:wght@400;600;700&display=swap">
<style>
  :root {
    --backdrop: #8d8f92;
    --brand-blue: #2466b0;
    --brand-blue-deep: #1b5296;
    --brand-blue-light: #3a7dc6;
    --card-white: #ffffff;
    --ink-grey: #6b6e72;
    --soft-grey: #d9dbde;
    --rule-grey: #b9bcc0;
  }
  * { box-sizing: border-box; margin: 0; padding: 0; }
  html, body { width: 1200px; height: 908px; overflow: hidden; }
  body {
    background: var(--backdrop);
    font-family: "Open Sans", Arial, sans-serif;
    position: relative;
  }
  .card {
    position: absolute;
    width: 540px;
    height: 309px;
    border-radius: 22px;
    overflow: hidden;
    box-shadow: 0 6px 18px rgba(0,0,0,0.25);
  }
  .card-front {
    left: 40px; top: 300px;
    background: linear-gradient(135deg, var(--brand-blue-light), var(--brand-blue) 50%, var(--brand-blue-deep));
    display: flex; align-items: center; justify-content: center;
  }
  .front-brand {
    display: flex; align-items: center; gap: 14px;
    color: var(--card-white);
  }
  .brand-square {
    width: 34px; height: 34px;
    background: var(--card-white);
  }
  .front-brand .brand-name {
    font-weight: 700; font-size: 25px; letter-spacing: 0.5px; text-transform: uppercase;
    line-height: 1.05;
  }
  .card-back {
    left: 620px; top: 300px;
    background: var(--card-white);
  }
  .back-brand {
    position: absolute; left: 34px; top: 82px;
    display: flex; align-items: center; gap: 10px;
    color: var(--brand-blue);
  }
  .back-brand .brand-square { background: var(--brand-blue); width: 24px; height: 24px; }
  .back-brand .brand-name {
    font-weight: 700; font-size: 17px; text-transform: uppercase; line-height: 1.1; width: 190px;
  }
  .divider {
    position: absolute; left: 262px; top: 62px; width: 1px; height: 110px;
    background: var(--rule-grey);
  }
  .contact-list {
    position: absolute; left: 278px; top: 66px; list-style: none;
    font-size: 10.5px; color: var(--ink-grey);
  }
  .contact-list li { display: flex; align-items: flex-start; gap: 7px; margin-bottom: 9px; line-height: 1.35; }
  .contact-list svg { flex: none; margin-top: 1px; }
  .person { position: absolute; left: 34px; top: 170px; }
  .person-name { color: var(--brand-blue); font-weight: 600; font-size: 17px; }
  .person-title { color: var(--rule-grey); font-size: 13px; }
  .bottom-band { position: absolute; left: 0; bottom: 0; }
  .website {
    position: absolute; right: 26px; bottom: 18px;
    color: var(--card-white); font-size: 12px; letter-spacing: 0.6px;
  }
</style>
</head>
<body>
  <section class="card card-front" aria-label="Card front">
    <div class="front-brand">
      <span class="brand-square"></span>
      <span class="brand-name">BrightPath<br>Learning Group</span>
    </div>
  </section>

  <section class="card card-back" aria-label="Card back">
    <div class="back-brand">
      <span class="brand-square"></span>
      <span class="brand-name">BrightPath Learning Group</span>
    </div>
    <div class="divider"></div>
    <ul class="contact-list">
      <li>
        <svg width="11" height="13" viewBox="0 0 11 13"><path d="M5.5 0C2.5 0 .5 2.2.5 4.8c0 3.3 5 8.2 5 8.2s5-4.9 5-8.2C10.5 2.2 8.5 0 5.5 0z" fill="#2466b0"/><circle cx="5.5" cy="4.8" r="1.8" fill="#fff"/></svg>
        <span>4-17-3 Hoshimidai, Adachi,<br>Tokyo 123-0845</span>
      </li>
      <li>
        <svg width="12" height="12" viewBox="0 0 12 12"><circle cx="6" cy="6" r="6" fill="#2466b0"/><path d="M4 3l1.2 1.4-.6.9c.4.9 1 1.5 1.9 1.9l.9-.6L8.8 8 8 9C5.6 8.7 3.3 6.4 3 4z" fill="#fff"/></svg>
        <span>(080) 5512-0476</span>
      </li>
      <li>
        <svg width="12" height="12" viewBox="0 0 12 12"><circle cx="6" cy="6" r="6" fill="#2466b0"/><rect x="3" y="4" width="6" height="4.2" fill="none" stroke="#fff" stroke-width="0.9"/><path d="M3 4l3 2.3L9 4" fill="none" stroke="#fff" stroke-width="0.9"/></svg>
        <span>brandon@brightpathlearninggroup.example</span>
      </li>
    </ul>
    <div class="person">
      <p class="person-name">Brandon Mallory</p>
      <p class="person-title">President</p>
    </div>
    <svg class="bottom-band" width="540" height="100" viewBox="0 0 540 100">
      <path d="M0 28 C120 70 300 66 540 36 L540 100 L0 100 Z" fill="#d9dbde"/>
      <path d="M0 44 C140 82 320 78 540 50 L540 100 L0 100 Z" fill="#2466b0"/>
    </svg>
    <p class="website">www.BrightPathLearningGroup.example</p>
  </section>
</body>
</html>
```